Entertainment Sound and Lighting company Business card

We need a professional looking business card designed for my growing entertainment sound and lighting company based in Sydney, Australia called "Kestrel Sound"

We provide technical production services (sound systems/lighting/vision) for events ranging from band gigs, weddings, corporate functions etc.

The business card needs to contain the following information:

Bartholomew Quenneville
Audio Engineer
Phone: 0478 615 702
Email: bartholomew@kestrelsound.com.au
Website: www.kestrelsound.com.au

Business logo has been attached in .ai format, please contact me if you need me to provide other files.

Target Market(s)

We need a business card that reflects our modern and professional company but still looks professional to appeal to our corporate clients.
We have a very broad target market spanning from bands needing PA systems for their gigs (18-30yrs) to event companies needing sound and lighting for weddings and other functions.

Industry/Entity Type

Business

Requirements
Must have
• Needs to include the logo that is attached of course, and the colour scheme.
Nice to have
• - Double sided

```html
<!DOCTYPE html>
<html lang="en">
<head>
<meta charset="utf-8">
<title>Kestrel Sound – Business Card</title>
<link href="https://fonts.googleapis.com/css2?family=Arimo:wght@400;700&display=swap" rel="stylesheet">
<style>
  :root {
    --page: #ffffff;
    --card: #000000;
    --ink-blue: #1ba3dc;
    --brand-blue: #1a86c8;
    --lamp-dark: #2a2f36;
    --lamp-light: #8fa4b4;
    --lamp-glow: #2fb6f0;
  }
  * { margin: 0; padding: 0; box-sizing: border-box; }
  html, body {
    width: 1200px;
    height: 800px;
    overflow: hidden;
    background: var(--page);
  }
  .canvas {
    position: relative;
    width: 1200px;
    height: 800px;
    font-family: "Arimo", Arial, sans-serif;
  }
  .card {
    position: absolute;
    background: var(--card);
    overflow: hidden;
  }
  .card--front {
    left: 44px;
    top: 40px;
    width: 572px;
    height: 372px;
  }
  .card--back {
    left: 636px;
    top: 430px;
    width: 524px;
    height: 342px;
  }
  .stage-light {
    position: absolute;
    left: 34px;
    top: 30px;
    width: 190px;
    height: 158px;
    border-radius: 40px 60px 30px 50px;
    background: radial-gradient(circle at 55% 45%, var(--lamp-glow) 0%, var(--lamp-light) 28%, var(--lamp-dark) 70%, var(--card) 100%);
  }
  .contact {
    position: absolute;
    left: 284px;
    top: 160px;
    color: var(--ink-blue);
    font-size: 14px;
    line-height: 17px;
    letter-spacing: 0.04em;
    white-space: nowrap;
  }
  .contact__name { margin-bottom: 14px; }
  .brand {
    position: absolute;
    left: 0;
    right: 0;
    top: 230px;
    display: flex;
    align-items: center;
    justify-content: center;
    gap: 18px;
  }
  .brand__dot {
    width: 34px;
    height: 34px;
    border-radius: 50%;
    background: var(--brand-blue);
  }
  .brand__name {
    color: var(--brand-blue);
    font-size: 56px;
    font-weight: 700;
    letter-spacing: -0.01em;
    line-height: 1;
    white-space: nowrap;
  }
</style>
</head>
<body>
  <main class="canvas">
    <section class="card card--front">
      <div class="stage-light" role="img" aria-label="Illustration of a chrome stage spotlight with blue lens and barn doors"></div>
      <div class="contact">
        <p class="contact__name">Bartholomew Quenneville</p>
        <p class="contact__role">Audio Engineer</p>
        <p class="contact__line">M: +0478 615 702</p>
        <p class="contact__line">E: bartholomew@kestrelsound.com.au</p>
        <p class="contact__line">W: www.kestrelsound.com.au</p>
      </div>
    </section>
    <section class="card card--back">
      <div class="brand">
        <span class="brand__dot"></span>
        <span class="brand__name">Kestrel Sound</span>
      </div>
    </section>
  </main>
</body>
</html>
```